Flyers

Modify Existing Flyer and create another for exterior company
Updates

Previous Brief has been updated- we want to update this existing one also

Target Market(s)

Exterior Remodeling Customers

Industry/Entity Type

Remodeling/Construction

```html
<!DOCTYPE html>
<html lang="en">
<head>
<meta charset="utf-8">
<title>Remodeling Flyer</title>
<link rel="stylesheet" href="https://fonts.googleapis.com/css2?family=Montserrat:wght@400;500;600;700;800;900&display=swap">
<style>
  :root {
    --page-bg: #d9d9d9;
    --paper: #ffffff;
    --brand-blue: #1f6bb5;
    --navy: #1b2f5c;
    --orange: #e2522a;
    --dark: #2a2a2a;
    --text: #3c3c3c;
    --kitchen-tone-a: #c8a07a;
    --kitchen-tone-b: #7a5a3e;
    --bath-tone-a: #3a3a3a;
    --bath-tone-b: #101010;
    --tub-tone-a: #f1e6d4;
    --tub-tone-b: #b9905a;
  }
  * { box-sizing: border-box; margin: 0; padding: 0; }
  html, body { width: 1200px; height: 674px; overflow: hidden; }
  body {
    background: var(--page-bg);
    font-family: "Montserrat", sans-serif;
    color: var(--text);
    position: relative;
  }
  .flyer {
    position: absolute;
    left: 352px; top: 17px;
    width: 495px; height: 640px;
    background: var(--paper);
    overflow: hidden;
    box-shadow: 0 4px 18px rgba(0,0,0,.18);
  }
  .abs { position: absolute; }

  .brand {
    left: 20px; top: 24px;
    display: flex; align-items: center; gap: 6px;
    font-weight: 700; font-size: 10px; color: var(--navy);
    text-transform: uppercase; letter-spacing: .3px;
  }
  .brand-dot { width: 10px; height: 10px; background: var(--orange); }

  .contact {
    right: 18px; top: 8px; text-align: right;
    font-size: 6px; letter-spacing: .6px; color: #777; text-transform: uppercase; line-height: 1.25;
  }
  .contact .phone { font-size: 14px; font-weight: 800; color: var(--navy); letter-spacing: 0; margin: 1px 0; line-height: 1.1; }
  .contact .web { text-transform: lowercase; }

  .header-shapes { left: 0; top: 0; width: 495px; height: 320px; }

  .photo-kitchen {
    left: 0; top: 0; width: 246px; height: 268px;
    background: linear-gradient(135deg, var(--kitchen-tone-a), var(--kitchen-tone-b));
    clip-path: polygon(0 110px, 100% 88px, 100% 100%, 0 100%);
  }
  .photo-bath {
    left: 250px; top: 0; width: 245px; height: 208px;
    background: linear-gradient(160deg, var(--bath-tone-a), var(--bath-tone-b));
    clip-path: polygon(0 88px, 100% 66px, 100% 100%, 0 100%);
  }
  .label-kitchen {
    left: 0; top: 236px; width: 246px; height: 32px;
    background: rgba(30,30,30,.88); color: #fff;
    font-weight: 800; font-size: 19px; padding: 4px 0 0 16px;
  }
  .label-bath {
    left: 250px; top: 174px; width: 245px; height: 34px;
    color: #fff; font-weight: 800; font-size: 21px; padding: 4px 0 0 14px;
  }
  .orange-side { left: 246px; top: 208px; width: 249px; height: 110px; background: var(--orange); }
  .orange-band {
    left: 0; top: 268px; width: 495px; height: 50px; background: var(--orange); color: #fff;
    padding: 5px 0 0 16px; line-height: 1.12;
  }
  .orange-band .lead { font-size: 9px; font-weight: 500; }
  .orange-band .title { font-size: 16px; font-weight: 800; }
  .orange-band .place { font-size: 9px; font-weight: 500; }

  .photo-tub {
    left: 336px; top: 192px; width: 128px; height: 128px; border-radius: 50%;
    background: radial-gradient(circle at 50% 45%, var(--tub-tone-a), var(--tub-tone-b));
    border: 4px solid var(--paper);
  }

  .section h2 {
    font-size: 11.5px; font-weight: 800; color: var(--navy); text-transform: uppercase; letter-spacing: .2px;
  }
  .section p { font-size: 7px; line-height: 1.3; margin-top: 2px; }
  .section ul { list-style: none; font-size: 7px; line-height: 1.4; }
  .section li::before {
    content: ""; display: inline-block; width: 4px; height: 4px; margin-right: 5px;
    border: 1px solid #999; vertical-align: 1px;
  }
  .cols { display: flex; gap: 18px; margin-top: 4px; }

  .kitchen { left: 22px; top: 338px; width: 300px; }
  .decks { left: 318px; top: 352px; width: 160px; }
  .additions { left: 22px; top: 450px; width: 290px; }
  .icon { width: 34px; height: 30px; }
  .icon-kitchen { left: 262px; top: 322px; }
  .icon-decks { left: 318px; top: 322px; }
  .icon-house { left: 250px; top: 434px; }

  .blue-band { left: 0; top: 500px; width: 495px; height: 140px; }
  .bath-remodel { left: 62px; top: 574px; width: 200px; color: #fff; }
  .bath-remodel h2 { color: #fff; }
  .bath-list { left: 282px; top: 564px; color: #fff; }
  .bath-list li::before { border-color: #cfe0f2; }
  .icon-bath { left: 18px; top: 588px; width: 36px; height: 32px; }
</style>
</head>
<body>
<main class="flyer">
  <div class="abs photo-kitchen" role="img" aria-label="Photo of a remodeled wood cabinet kitchen"></div>
  <div class="abs photo-bath" role="img" aria-label="Photo of a modern dark tiled bathroom with vanity"></div>

  <svg class="abs header-shapes" viewBox="0 0 495 320" aria-hidden="true">
    <polygon points="0,100 495,56 495,66 0,110" fill="var(--brand-blue)"/>
    <polygon points="246,88 250,88 250,268 246,268" fill="var(--paper)"/>
  </svg>

  <div class="abs brand"><span class="brand-dot"></span>Northfield Roofing and Exteriors</div>

  <div class="abs contact">
    Call today for your<br>free estimate
    <div class="phone">555-014-2290</div>
    <div class="web">www.northfieldexteriors.com</div>
  </div>

  <div class="abs label-kitchen">Kitchen</div>
  <div class="abs label-bath">Bathroom?</div>
  <div class="abs orange-side"></div>
  <div class="abs orange-band">
    <div class="lead">Work with a Top-rated Local</div>
    <div class="title">Remodeling Company</div>
    <div class="place">in Maple Falls, IA</div>
  </div>
  <div class="abs photo-tub" role="img" aria-label="Photo of a freestanding white bathtub"></div>

  <svg class="abs icon icon-kitchen" viewBox="0 0 34 30" fill="none" stroke="var(--orange)" stroke-width="1.5" aria-hidden="true">
    <rect x="3" y="12" width="28" height="16"/><line x1="3" y1="18" x2="31" y2="18"/><line x1="17" y1="12" x2="17" y2="28"/>
    <rect x="8" y="3" width="18" height="6"/>
  </svg>
  <section class="abs section kitchen">
    <h2>Kitchen Remodeling</h2>
    <p>Whatever your vision is for your new kitchen,<br>our crew can help you bring it to life. You can trust us for:</p>
    <div class="cols">
      <ul>
        <li>Open concept design services</li>
        <li>Kitchen cabinet installation services</li>
        <li>Kitchen countertop installation services</li>
        <li>Lighting installation services</li>
        <li>Tile installation services</li>
      </ul>
      <ul>
        <li>Plumbing upgrade services</li>
        <li>Electrical upgrade services</li>
        <li>Drywall services</li>
        <li>Painting services</li>
      </ul>
    </div>
  </section>

  <svg class="abs icon icon-decks" viewBox="0 0 34 30" fill="none" stroke="var(--orange)" stroke-width="1.5" aria-hidden="true">
    <path d="M4 12 Q17 0 30 12 Z"/><line x1="17" y1="12" x2="17" y2="28"/>
    <line x1="6" y1="22" x2="28" y2="22"/><line x1="8" y1="22" x2="6" y2="28"/><line x1="26" y1="22" x2="28" y2="28"/>
  </svg>
  <section class="abs section decks">
    <h2>Decks/Patios</h2>
    <p>An outdoor space is a great addition to any residential property. When you decide to build a patio or deck, you'll be able to experience a variety of benefits. Your outdoor area will increase your:</p>
    <ul style="margin-top:4px">
      <li>Property value</li>
      <li>Curb appeal</li>
      <li>Functional living space</li>
    </ul>
  </section>

  <svg class="abs icon icon-house" viewBox="0 0 34 30" fill="none" stroke="var(--orange)" stroke-width="1.5" aria-hidden="true">
    <polyline points="3,15 17,3 31,15"/><rect x="7" y="13" width="20" height="15"/><rect x="14" y="19" width="6" height="9"/>
  </svg>
  <section class="abs section additions">
    <h2>Home Additions</h2>
    <p>No matter what kind of space you need,<br>our team will bring your vision to life. You<br>can hire us if you need a:</p>
    <div class="cols">
      <ul>
        <li>Bathroom addition</li>
        <li>Bedroom addition</li>
        <li>Garage addition</li>
        <li>Basement addition</li>
      </ul>
      <ul>
        <li>Guest room addition</li>
        <li>Living room addition</li>
        <li>Sunroom addition</li>
      </ul>
    </div>
  </section>

  <svg class="abs blue-band" viewBox="0 0 495 140" aria-hidden="true">
    <polygon points="0,70 495,36 495,140 0,140" fill="var(--brand-blue)"/>
  </svg>
  <svg class="abs icon-bath" viewBox="0 0 36 32" fill="none" stroke="#fff" stroke-width="1.5" aria-hidden="true">
    <path d="M3 16 H33 V20 Q33 27 25 27 H11 Q3 27 3 20 Z"/><path d="M7 16 V6 Q7 3 10 3 Q13 3 13 6"/>
    <line x1="9" y1="27" x2="8" y2="30"/><line x1="27" y1="27" x2="28" y2="30"/>
  </svg>
  <section class="abs section bath-remodel">
    <h2>Bathroom Remodeling</h2>
    <p>When you hire us for your bathroom remodeling project, the possibilities are endless. Our experienced and talented team can:</p>
  </section>
  <section class="abs section bath-list">
    <ul>
      <li>Install a custom tile shower</li>
      <li>Build a new vanity</li>
      <li>Install flooring and tile</li>
      <li>Replace your plumbing and light fixtures</li>
    </ul>
  </section>
</main>
</body>
</html>
```